Marketing Flyer for General Contractor

1. General Layout: 8.5" x 11
Front Page: Introduce our services with a strong, attention-grabbing header. Use icons or special bullet points to list the services, making them stand out. (See PDf for content)
Back Page: Provide detailed descriptions and benefits, organized in a clean and structured manner. Include testimonials or client success stories if available. (See PDF for Content)
2. Design Elements:
Color Scheme: Incorporate blue, black, white, red, yellow, and turquoise. Additional colors can be used if they enhance the design.
Icons/Bullet Points: Use creative and visually appealing icons or bullet points for the services list on the front page.
Images: Use the uploaded images and incorporate high-quality stock images where necessary. I am willing to purchase stock images if they enhance the layout.
QR Code: Include a QR code with the phone number and website in the footer on both pages.
Contact Info: Ensure the contact information stands out and is easy to find and read.
3. Specific Instructions for Content:
Front Page:
Header: Create a bold and eye-catching title that communicates our expertise in helping realtors enhance listings.
Services List: Use icons or special bullet points to make each service stand out. Ensure the text is clear and easy to read.
Contact Info: Prominently display the phone number and website, with a QR code at the bottom.
Back Page:
Detailed Descriptions: Organize the content logically, using headings and subheadings to break up the text. Make it easy to scan and read.
Benefits and Value Statements: Highlight the key benefits and value propositions in bold or larger font to draw attention.
Testimonials/Success Stories: If space allows, include one or two testimonials or success stories.
Contact Info: Again, prominently display the phone number and website, with a QR code at the bottom.
4. Typography:
Use clear, readable fonts. Mix bold and regular fonts to emphasize key points and maintain a professional look.
5. Additional Notes:
Ensure the overall design is balanced and not too cluttered.
Maintain a professional yet inviting aesthetic that appeals to realtors.
The flyer should convey confidence and expertise, encouraging realtors to choose our services.
Low design quality
Real estate agents
Construction General Contractor

```html
<!DOCTYPE html>
<html lang="en">
<head>
<meta charset="utf-8">
<title>Coastline Remodel Co. – Realtor Flyer</title>
<link rel="stylesheet" href="https://fonts.googleapis.com/css2?family=Montserrat:wght@400;500;700;800;900&family=Open+Sans:wght@400;600&display=swap">
<style>
  :root{
    --page-bg:#f4f5f2;
    --paper:#ffffff;
    --ink:#111111;
    --brand-blue:#3a86e8;
    --accent-orange:#f7941d;
    --band-navy:#1a2133;
    --band-dark:#121315;
    --label:#e9e9e9;
  }
  *{margin:0;padding:0;box-sizing:border-box}
  html,body{width:1200px;height:2351px;overflow:hidden;background:var(--page-bg)}
  .flyer{position:absolute;left:50px;top:464px;width:1100px;height:1423px;background:var(--paper);overflow:hidden;box-shadow:0 20px 60px rgba(0,0,0,.18);font-family:"Montserrat",sans-serif}
  .hero-photo{position:absolute;left:0;top:0;width:1100px;height:757px;
    background:linear-gradient(180deg,#dfe4ea 0%,#eef1f4 40%,#cfd4d8 72%,#b9bec2 100%)}
  .hero-panel{position:absolute;left:92px;top:0;width:894px;height:300px;
    background:linear-gradient(180deg,#fff 0%,#fff 70%,rgba(255,255,255,0) 100%)}
  .brand{position:absolute;left:0;right:0;top:120px;display:flex;justify-content:center;align-items:center;gap:14px}
  .brand-square{width:22px;height:22px;background:var(--ink)}
  .brand-name{font-weight:500;font-size:30px;letter-spacing:2px;color:var(--ink);text-transform:uppercase}
  .tagline-pill{position:absolute;left:228px;top:252px;width:646px;height:41px;border-radius:6px;background:var(--brand-blue);
    color:#fff;font-weight:800;font-size:27px;text-align:center;line-height:41px;letter-spacing:.5px}
  .headline{position:absolute;left:0;right:0;text-align:center;font-weight:800;line-height:1}
  .headline-experts{top:312px;font-size:64px;color:var(--ink)}
  .headline-realtor{top:383px;font-size:88px;color:var(--brand-blue);font-weight:900}
  .headline-contractor{top:473px;font-size:34px;color:var(--ink);font-weight:700}
  .services-band{position:absolute;left:0;top:757px;width:1100px;height:582px;
    background:linear-gradient(180deg,var(--band-navy) 0%,var(--band-navy) 25%,var(--band-dark) 32%,#1c1c1c 70%,var(--band-dark) 100%)}
  .guarantee{position:absolute;left:0;right:0;top:786px;text-align:center;color:var(--accent-orange);font-weight:900;font-size:42px}
  .specializing{position:absolute;left:0;right:0;top:840px;text-align:center;color:#fff;font-weight:400;font-size:38px}
  .service{position:absolute;width:190px;margin-left:-95px;text-align:center}
  .service-icon{display:block;width:88px;height:88px;margin:0 auto}
  .service-label{margin-top:14px;font-family:"Open Sans",sans-serif;font-size:19px;line-height:1.25;color:var(--label)}
  .row-1{top:946px}
  .row-2{top:1134px}
  .web{position:absolute;left:0;right:0;top:1358px;text-align:center;font-weight:500;font-size:32px;letter-spacing:4px;color:var(--ink)}
</style>
</head>
<body>
<main class="flyer">
  <div class="hero-photo" role="img" aria-label="Bright modern open-plan living room with a white sectional sofa, coffee table, plants and sea-view windows"></div>
  <div class="hero-panel"></div>

  <div class="brand"><span class="brand-square"></span><span class="brand-name">Coastline Remodel Co.</span></div>

  <div class="tagline-pill">REAL PROS, REAL ADVICE, REAL VALUE.</div>
  <h1 class="headline headline-experts">REMODELING EXPERTS</h1>
  <h2 class="headline headline-realtor">REALTOR’S #1</h2>
  <h3 class="headline headline-contractor">GENERAL CONTRACTOR</h3>

  <section class="services-band" role="img" aria-label="Dark interior photo backdrop"></section>
  <p class="guarantee">OUR SERVICES ARE 100% GUARANTEED</p>
  <p class="specializing">SPECIALIZING IN:</p>

  <div class="service row-1" style="left:170px">
    <svg class="service-icon" viewBox="0 0 88 88"><circle cx="44" cy="44" r="44" fill="#f7941d"/><rect x="31" y="23" width="26" height="42" rx="3" fill="#fff"/><rect x="31" y="38" width="26" height="2.5" fill="#f7941d"/><rect x="35" y="29" width="2.5" height="6" fill="#f7941d"/><rect x="35" y="44" width="2.5" height="8" fill="#f7941d"/></svg>
    <p class="service-label">Kitchen<br>Remodel</p>
  </div>
  <div class="service row-1" style="left:321px">
    <svg class="service-icon" viewBox="0 0 88 88"><circle cx="44" cy="44" r="44" fill="#f7941d"/><path d="M30 64V32a8 8 0 0 1 16 0v2" stroke="#fff" stroke-width="4" fill="none"/><path d="M40 36h14l-7 8z" fill="#fff"/><g fill="#fff"><circle cx="50" cy="50" r="2"/><circle cx="56" cy="48" r="2"/><circle cx="62" cy="46" r="2"/><circle cx="53" cy="56" r="2"/><circle cx="59" cy="54" r="2"/><circle cx="56" cy="61" r="2"/></g></svg>
    <p class="service-label">Bathroom<br>Remodel</p>
  </div>
  <div class="service row-1" style="left:500px">
    <svg class="service-icon" viewBox="0 0 88 88"><circle cx="44" cy="44" r="44" fill="#f7941d"/><rect x="44" y="18" width="8" height="24" rx="3" fill="#fff" transform="rotate(30 48 30)"/><path d="M30 50l16 9-6 10c-6-1-13-5-16-10z" fill="#fff"/><rect x="35" y="40" width="14" height="10" fill="#fff" transform="rotate(30 42 45)"/></svg>
    <p class="service-label">‘Painting:<br>Interior/ Exterior:</p>
  </div>
  <div class="service row-1" style="left:687px">
    <svg class="service-icon" viewBox="0 0 88 88"><circle cx="44" cy="44" r="44" fill="#f7941d"/><g fill="#fff"><rect x="26" y="26" width="16" height="8"/><rect x="44" y="26" width="18" height="8"/><rect x="26" y="36" width="8" height="16"/><rect x="36" y="36" width="16" height="16"/><rect x="54" y="36" width="8" height="16"/><rect x="26" y="54" width="18" height="8"/><rect x="46" y="54" width="16" height="8"/></g></svg>
    <p class="service-label">Flooring: Carpet,<br>Vinyl, Wood</p>
  </div>
  <div class="service row-1" style="left:880px">
    <svg class="service-icon" viewBox="0 0 88 88"><circle cx="44" cy="44" r="44" fill="#f7941d"/><path d="M30 66V22h24v44" stroke="#fff" stroke-width="4" fill="none"/><path d="M34 24l14 6v38l-14-4z" fill="#fff"/><rect x="56" y="64" width="8" height="3" fill="#fff"/><circle cx="43" cy="46" r="2" fill="#f7941d"/></svg>
    <p class="service-label">Window and Door<br>Replacement</p>
  </div>

  <div class="service row-2" style="left:170px">
    <svg class="service-icon" viewBox="0 0 88 88"><circle cx="44" cy="44" r="44" fill="#f7941d"/><path d="M60 28H34a8 8 0 0 0 0 16h20a8 8 0 0 1 0 16H26" stroke="#fff" stroke-width="9" fill="none"/><rect x="58" y="22" width="6" height="12" fill="#fff"/><rect x="24" y="54" width="6" height="12" fill="#fff"/></svg>
    <p class="service-label">Plumbing<br>Repairs and<br>Upgrades</p>
  </div>
  <div class="service row-2" style="left:321px">
    <svg class="service-icon" viewBox="0 0 88 88"><circle cx="44" cy="44" r="44" fill="#f7941d"/><path d="M60 20a12 12 0 0 0-14 15L24 57a5 5 0 0 0 7 7l22-22a12 12 0 0 0 15-14l-7 7-6-2-2-6z" fill="#fff"/></svg>
    <p class="service-label">‘Energy-Efficient<br>Upgrades</p>
  </div>
  <div class="service row-2" style="left:500px">
    <svg class="service-icon" viewBox="0 0 88 88"><circle cx="44" cy="44" r="44" fill="#f7941d"/><path d="M28 24l8-2 6 6-4 4zM36 32l28 28-4 4-28-28z" fill="#fff"/><path d="M60 22a9 9 0 0 0-10 11L26 57a4 4 0 0 0 6 6l24-24a9 9 0 0 0 11-10l-5 5-5-1-1-5z" fill="#fff"/></svg>
    <p class="service-label">‘Deck &amp; Patio<br>Construction</p>
  </div>
  <div class="service row-2" style="left:687px">
    <svg class="service-icon" viewBox="0 0 88 88"><circle cx="44" cy="44" r="44" fill="#f7941d"/><path d="M22 40l22-18 22 18v26H22z" stroke="#fff" stroke-width="4" fill="none" stroke-linejoin="round"/><rect x="31" y="42" width="26" height="20" fill="none" stroke="#fff" stroke-width="3"/><rect x="34" y="50" width="20" height="8" rx="3" fill="#fff"/></svg>
    <p class="service-label">Garage<br>Renovation</p>
  </div>
  <div class="service row-2" style="left:880px">
    <svg class="service-icon" viewBox="0 0 88 88"><circle cx="44" cy="44" r="44" fill="#f7941d"/><rect x="40" y="46" width="24" height="18" fill="#fff"/><path d="M52 46c-8-4-8-14 0-18 8 4 8 14 0 18z" fill="#fff"/><path d="M30 44v20M24 64h14" stroke="#fff" stroke-width="4"/></svg>
    <p class="service-label">‘Landscaping</p>
  </div>

  <p class="web">www.HarborlineRemodel.com</p>
</main>
</body>
</html>
```